Velmira Body Oil Label for 4 -8 oz bottles

We are selling 4 and 8 oz body oils and need a label to put on our bottles. I'm not sure if we want a label for the front and also the back of the bottle or just one label in the front. You can give me examples of each way. Attached is our logo on a blue background but the background will change colors depending on the scent as specified in the design description. Our bottle will be either clear or white with a pump spray type lid as shown in the attached example. Attached are also our design criteria which is needed for the labels.
Updates

We have decided to use the disc top cap and not the pump spray cap. If you are able to, please show us the design on the 4 oz bottle with the disc top cap. Thanks

Target Market(s)

women

Industry/Entity Type

skincare, cosmetics

Font styles to use
Serif
Sans Serif

Requirements
Must have
• stylish name for each scented oil which contrasts the font in the logo. Also must have darker colors since the logo colors are lighter.
Nice to have
• Border around the labels, maybe one solid color or maybe two complimenting colors which go well with the fragrnace name
Should not have
• background colors that match the logo colors

```html
<!DOCTYPE html>
<html lang="en">
<head>
<meta charset="utf-8">
<title>Velmira Cotton Candy Body Oil Label</title>
<link rel="stylesheet" href="https://fonts.googleapis.com/css2?family=Montserrat:wght@500;600&family=Bellefair&family=Encode+Sans+Condensed:wght@400;700&display=swap">
<style>
  :root {
    --backdrop-light: #fff1cf;
    --backdrop-warm: #fdd58f;
    --turquoise: #05c9e0;
    --turquoise-light: #5de3f0;
    --candy-pink: #f38ac9;
    --candy-pink-light: #f9b3dc;
    --label-white: #ffffff;
    --accent-gold: #e9c97d;
  }
  * { margin: 0; padding: 0; box-sizing: border-box; }
  html, body { width: 1200px; height: 1200px; overflow: hidden; }
  body {
    background: radial-gradient(circle at 50% 50%, var(--backdrop-light) 0%, var(--backdrop-warm) 100%);
    position: relative;
  }
  .label {
    position: absolute;
    left: 227px;
    top: 84px;
    width: 746px;
    height: 1032px;
    box-shadow: 0 10px 30px rgba(170, 120, 40, 0.18);
  }
  .label svg { display: block; width: 100%; height: 100%; }
  .brand-name {
    font-family: "Montserrat", sans-serif;
    font-weight: 600;
    font-size: 96px;
    fill: var(--label-white);
    letter-spacing: 2px;
  }
  .scent-name {
    font-family: "Montserrat", sans-serif;
    font-weight: 500;
    font-size: 146px;
    letter-spacing: -3px;
  }
  .product-type {
    font-family: "Bellefair", serif;
    font-size: 90px;
    fill: var(--turquoise);
  }
  .benefits {
    font-family: "Encode Sans Condensed", sans-serif;
    font-weight: 400;
    font-size: 25px;
    fill: var(--label-white);
  }
  .net-weight {
    font-family: "Encode Sans Condensed", sans-serif;
    font-weight: 700;
    font-size: 30px;
    fill: var(--label-white);
  }
</style>
</head>
<body>
  <div class="label">
    <svg viewBox="0 0 746 1032" xmlns="http://www.w3.org/2000/svg">
      <defs>
        <linearGradient id="turquoiseFill" x1="0" y1="0" x2="1" y2="0">
          <stop offset="0" stop-color="var(--turquoise)"/>
          <stop offset="0.5" stop-color="var(--turquoise-light)"/>
          <stop offset="1" stop-color="var(--turquoise)"/>
        </linearGradient>
        <linearGradient id="pinkFill" x1="0" y1="0" x2="1" y2="0">
          <stop offset="0" stop-color="var(--candy-pink)"/>
          <stop offset="0.5" stop-color="var(--candy-pink-light)"/>
          <stop offset="1" stop-color="var(--candy-pink)"/>
        </linearGradient>
        <linearGradient id="scentFill" x1="0" y1="0" x2="0" y2="1">
          <stop offset="0" stop-color="var(--candy-pink)"/>
          <stop offset="1" stop-color="var(--candy-pink-light)"/>
        </linearGradient>
      </defs>

      <rect class="label-base" x="0" y="0" width="746" height="800" fill="url(#turquoiseFill)"/>
      <rect class="label-footer" x="0" y="800" width="746" height="232" fill="url(#pinkFill)"/>

      <g class="brand-mark">
        <circle cx="373" cy="148" r="26" fill="var(--accent-gold)"/>
        <text class="brand-name" x="373" y="290" text-anchor="middle">Velmira</text>
      </g>

      <path class="name-panel" fill="var(--label-white)"
        d="M52,456 Q52,402 106,402 H640 Q694,402 694,456 V745 Q694,777 726,777 H746 V800 H0 V777 H20 Q52,777 52,745 Z"/>
      <path class="name-tab" fill="var(--label-white)"
        d="M120,799 Q150,799 160,822 Q170,858 205,858 H541 Q576,858 586,822 Q596,799 626,799 Z"/>

      <text class="scent-name" x="373" y="585" text-anchor="middle" fill="url(#scentFill)">COTTON</text>
      <text class="scent-name" x="373" y="735" text-anchor="middle" fill="url(#scentFill)">CANDY</text>
      <text class="product-type" x="373" y="842" text-anchor="middle">Body Oil</text>

      <g class="benefit-line">
        <text class="benefits" x="107" y="918" text-anchor="middle">Non-Greesy</text>
        <circle cx="198" cy="910" r="7" fill="var(--turquoise)"/>
        <text class="benefits" x="330" y="918" text-anchor="middle">With Vitamin E</text>
        <circle cx="470" cy="910" r="7" fill="var(--turquoise)"/>
        <text class="benefits" x="605" y="918" text-anchor="middle">Ultra Moisturizing</text>
      </g>
      <text class="net-weight" x="373" y="990" text-anchor="middle">Net Wt. 4 fl. oz. (118 mL)</text>
    </svg>
  </div>
</body>
</html>
```